Golden Years Wellness Map: This is my second book. The first was Elder Care Compass

I need a book cover design for: GOLDEN YEARS WELLNESS MAP: A NO-FEE METHOD FOR FINISHING YOUR LATER-LIFE JIGSAW THROUGH POOLED CARE SAVINGS ACCOUNTS by Derek Follard Ross Pellick & Martin Guvel. This book is designed for business owners, CEO's, CFO's and Human Resources. The cover needs to be professional and focused on business. The purpose of this book is to educate business owners and their management about a zero cost retiree health plan. This is a first of it's kind solution that every business needs to learn about.

Target Market(s)

Business owners, CEO's, CFO's and Human Resources

Requirements
Nice to have
• I want the design to be clean and professional since it is focused on business executives

```html
<!DOCTYPE html>
<html lang="en">
<head>
<meta charset="utf-8">
<title>Golden Years Wellness Map – Book Cover</title>
<link rel="stylesheet" href="https://fonts.googleapis.com/css2?family=Roboto+Condensed:wght@400;700;800&display=swap">
<style>
  :root {
    --stage: #3a271d;
    --paper: #eceadf;
    --slate: #6f8795;
    --gold: #c99f4f;
    --teal: #88aba1;
    --ink: #3d5260;
  }
  * { margin: 0; padding: 0; box-sizing: border-box; }
  html, body {
    width: 1200px;
    height: 554px;
    overflow: hidden;
    background: var(--stage);
  }
  .stage {
    width: 1200px;
    height: 554px;
    display: flex;
    align-items: center;
    justify-content: center;
  }
  .cover {
    position: relative;
    width: 369px;
    height: 554px;
    background: var(--paper);
    font-family: "Roboto Condensed", "Arial Narrow", sans-serif;
    text-align: center;
  }
  .title {
    position: absolute;
    top: 40px;
    left: 0;
    width: 100%;
    font-weight: 800;
    font-size: 48px;
    line-height: 51px;
    letter-spacing: 0.5px;
    text-transform: uppercase;
  }
  .title-line { display: block; color: var(--slate); }
  .title-line--accent { color: var(--gold); }
  .cover-art {
    position: absolute;
    top: 206px;
    left: 64px;
    width: 242px;
    height: 206px;
    border-radius: 46% 54% 48% 52% / 40% 46% 54% 60%;
    background: radial-gradient(circle at 45% 45%, var(--slate) 0%, var(--teal) 55%, #a9c3b9 100%);
  }
  .subtitle {
    position: absolute;
    top: 428px;
    left: 18px;
    right: 18px;
    color: var(--slate);
    font-weight: 400;
    font-size: 15.5px;
    line-height: 17px;
    letter-spacing: 0.2px;
    text-transform: uppercase;
  }
  .rule {
    position: absolute;
    top: 495px;
    left: 147px;
    width: 75px;
    height: 2px;
    background: var(--gold);
  }
  .authors {
    position: absolute;
    top: 503px;
    left: 0;
    width: 100%;
    color: var(--slate);
    font-weight: 400;
    font-size: 11px;
    line-height: 12.5px;
    text-transform: uppercase;
  }
</style>
</head>
<body>
  <main class="stage">
    <article class="cover">
      <h1 class="title">
        <span class="title-line">Golden Years</span>
        <span class="title-line title-line--accent">Wellness</span>
        <span class="title-line">Map</span>
      </h1>
      <div class="cover-art" role="img" aria-label="Illustration of a rolled-out blueprint with jigsaw pieces, a heart with a medical cross and a small bar chart"></div>
      <p class="subtitle">A no-fee method for finishing your later-life jigsaw through pooled care savings accounts</p>
      <div class="rule"></div>
      <p class="authors">By Derek Follard<br>Ross Pellick &amp; Martin Guvel</p>
    </article>
  </main>
</body>
</html>
```